Updated Logo, New Marketing Brochure, & New Business Cards

Hello! I actually have a few things I need some assistance with. I want to make some minor tweaks to my current branding and logo design. I believe I have the vector file- but the previous graphic designer I worked with through gigrunn did not give me everything I paid for, and stopped responding to my messages. So, I don’t want to work with her again.

I also need new business cards using this branding change, as well as some brochures to handout to doctors offices and other businesses that I am marketing my teen counseling services to.

Here is my practice’s site to get an idea of my current branding
www.LanternSkye.com

I would love an idea on budget and timeframe! Thankyou so much.
-Marisol

Target Market(s)

Teen Girls needing Counseling Services

Industry/Entity Type

Counsellor

Requirements
Must have
• My current branding colors and logo design with some minor alterations. A fresh layout for brochures that draws interest, while quickly speaking to the needs of the parents and teen girls that I serve.

```html
<!DOCTYPE html>
<html lang="en">
<head>
<meta charset="utf-8">
<title>LanternSkye Brochure</title>
<link href="https://fonts.googleapis.com/css2?family=Open+Sans:wght@400;600;700&family=Oswald:wght@400;700&display=swap" rel="stylesheet">
<style>
:root{
  --teal:#2e9c96;
  --teal-dark:#1f7f7a;
  --teal-light:#7fc9c3;
  --ink:#4a4a4a;
  --paper:#ffffff;
  --stage:#e9eaea;
  --pill:#8d8d8d;
}
*{box-sizing:border-box;margin:0;padding:0}
html,body{width:800px;height:1200px;overflow:hidden;background:var(--stage);font-family:"Open Sans",Arial,sans-serif;color:var(--ink)}
.canvas{position:relative;width:800px;height:1200px}
.spread{position:absolute;left:20px;width:760px;height:520px;display:flex;box-shadow:0 4px 14px rgba(0,0,0,.15)}
.spread--cover{top:40px}
.spread--inside{top:640px}
.page{position:relative;width:380px;height:520px;background:var(--paper);overflow:hidden}
.page + .page{border-left:1px solid #e2e2e2}
.page svg.bg{position:absolute;inset:0;width:380px;height:520px}
.heading{font-weight:700;color:var(--teal);font-size:10px;letter-spacing:.3px;margin:8px 0 4px}
.body{font-size:7px;line-height:1.45}
.body p{margin-bottom:5px}
p.body{margin-bottom:5px}
.ticks{list-style:none;font-size:7px;line-height:1.45}
.ticks li{position:relative;padding-left:14px;margin-bottom:4px}
.ticks li svg{position:absolute;left:0;top:1px;width:9px;height:9px}
.bullets{list-style:none;font-size:7px;line-height:1.45;margin-bottom:5px}
.bullets li{position:relative;padding-left:9px;margin-bottom:3px}
.bullets li::before{content:"";position:absolute;left:1px;top:4px;width:4px;height:4px;border-radius:50%;background:var(--teal)}
.about{position:absolute;left:26px;top:26px;width:330px}
.brand{font-weight:600;color:var(--teal);font-size:22px;letter-spacing:.3px}
.brand small{display:block;font-size:8px;font-weight:600;color:var(--teal);letter-spacing:.2px}
.contact{position:absolute;left:208px;top:290px;width:165px;color:#fff}
.contact .brand{color:#fff;font-size:18px;margin-bottom:10px}
.contact .brand small{color:#fff}
.contact-row{display:flex;align-items:flex-start;gap:7px;font-weight:700;font-size:8.5px;margin-bottom:8px}
.contact-row svg{flex:0 0 12px;width:12px;height:12px;margin-top:1px}
.contact-row.phone{font-size:12px}
.cover-brand{position:absolute;top:28px;left:0;width:380px;text-align:center}
.cover-title{position:absolute;left:0;top:392px;width:380px;text-align:center;color:#fff}
.cover-title h1{font-family:"Oswald",Impact,sans-serif;font-weight:700;font-size:27px;letter-spacing:.5px;line-height:1.1}
.cover-title h2{font-family:"Oswald",Arial,sans-serif;font-weight:400;font-size:17px;letter-spacing:.5px;margin-top:2px}
.pill{display:inline-block;margin-top:12px;background:var(--pill);color:#fff;font-size:8px;letter-spacing:4px;padding:4px 22px;border-radius:10px}
.tag{display:inline-block;background:var(--teal);color:#fff;font-weight:700;font-size:10px;padding:3px 14px 3px 10px;clip-path:polygon(0 0,100% 0,90% 100%,0 100%)}
.col{position:absolute}
</style>
</head>
<body>
<main class="canvas">

  <section class="spread spread--cover">
    <article class="page page--back">
      <svg class="bg" viewBox="0 0 380 520" aria-hidden="true">
        <path d="M0,300 C120,250 250,215 380,225 V520 H0 Z" fill="var(--teal)"/>
      </svg>
      <svg class="bg" viewBox="0 0 380 520">
        <circle cx="92" cy="410" r="100" fill="#fff"/>
        <defs><linearGradient id="mugPhoto" x1="0" y1="0" x2="1" y2="1"><stop offset="0" stop-color="#a5574a"/><stop offset=".5" stop-color="#d9b59a"/><stop offset="1" stop-color="#3d4f6b"/></linearGradient></defs>
        <circle cx="92" cy="410" r="93" fill="url(#mugPhoto)" role="img" aria-label="Photo of two people seated together, one holding a coffee mug"/>
      </svg>
      <div class="about">
        <h3 class="heading">ABOUT US :</h3>
        <div class="body">
          <p>My goal is for LanternSkye, LLC to not be your typical counseling practice. I seek to provide specialized services to women and teenage girls in more than just one way. It is important to me that you understand how much I get how very different and unique the healing process can be for each individual.</p>
          <p>That is why this is a counseling practice devoted to offering support, hope, and healing to women and teenage girls in numerous ways. Sometimes you're just not ready to jump into therapy, and that's ok! Here are a few services that will hopefully meet your needs:</p>
        </div>
        <ul class="ticks">
          <li><svg viewBox="0 0 10 10"><circle cx="5" cy="5" r="4.3" fill="none" stroke="var(--teal)" stroke-width="1"/><path d="M3,5.2 L4.5,6.6 L7.2,3.6" fill="none" stroke="var(--teal)" stroke-width="1.1"/></svg>Coming to one of my free local evening talks in the Open Door Circle series. Cost: FREE.</li>
          <li><svg viewBox="0 0 10 10"><circle cx="5" cy="5" r="4.3" fill="none" stroke="var(--teal)" stroke-width="1"/><path d="M3,5.2 L4.5,6.6 L7.2,3.6" fill="none" stroke="var(--teal)" stroke-width="1.1"/></svg>Scheduling an initial session to see if I can help you achieve a more balanced and joyful life. Weekly, biweekly, and intensive sessions are available.</li>
          <li><svg viewBox="0 0 10 10"><circle cx="5" cy="5" r="4.3" fill="none" stroke="var(--teal)" stroke-width="1"/><path d="M3,5.2 L4.5,6.6 L7.2,3.6" fill="none" stroke="var(--teal)" stroke-width="1.1"/></svg>Joining one of my LanternSkye groups where you can find community and support with like-minded women who are working to care for themselves.</li>
        </ul>
        <div class="body">
          <p>Over and over in my life I have met women and teenage girls who struggle with a low sense of worth and toxic shame. I would see them measuring their value by the time and energy spent on others. You matter, and you will run empty if you never pour into yourself.</p>
        </div>
      </div>
      <div class="contact">
        <div class="brand">LanternSkye<small>Support for Women and Teenage Girls</small></div>
        <div class="contact-row phone"><svg viewBox="0 0 12 12"><path d="M2.5,1 L4.5,1 L5.2,3.6 L4,4.6 C4.6,6 6,7.4 7.4,8 L8.4,6.8 L11,7.5 L11,9.5 C11,10.3 10.3,11 9.5,11 C5,11 1,7 1,2.5 C1,1.7 1.7,1 2.5,1 Z" fill="#fff"/></svg>615-555-0142</div>
        <div class="contact-row"><svg viewBox="0 0 12 12"><g fill="none" stroke="#fff" stroke-width="1"><circle cx="6" cy="6" r="5"/><ellipse cx="6" cy="6" rx="2.2" ry="5"/><path d="M1,6 H11 M2,3.5 H10 M2,8.5 H10"/></g></svg>www.LanternSkye.com</div>
        <div class="contact-row"><svg viewBox="0 0 12 12"><path d="M6,0.8 C3.8,0.8 2.2,2.5 2.2,4.5 C2.2,7.3 6,11.2 6,11.2 C6,11.2 9.8,7.3 9.8,4.5 C9.8,2.5 8.2,0.8 6,0.8 Z" fill="#fff"/><circle cx="6" cy="4.5" r="1.4" fill="var(--teal)"/></svg>4410 Meadowlark Ave, Suite 200<br>Franklin, TN 37064</div>
      </div>
    </article>

    <article class="page page--cover">
      <svg class="bg" viewBox="0 0 380 520">
        <defs><linearGradient id="heroPhoto" x1="0" y1="0" x2="0" y2="1"><stop offset="0" stop-color="#f3f0e3"/><stop offset=".5" stop-color="#c9c6b3"/><stop offset="1" stop-color="#6d7a55"/></linearGradient></defs>
        <rect width="380" height="520" fill="var(--teal)"/>
        <path d="M0,0 H380 V270 C300,340 170,350 0,330 Z" fill="var(--teal-light)"/>
        <path d="M0,0 H380 V258 C300,330 170,338 0,320 Z" fill="url(#heroPhoto)" role="img" aria-label="Photo of a woman with arms outstretched on a grassy hillside"/>
      </svg>
      <div class="cover-brand"><div class="brand">LanternSkye<small>Support for Women and Teenage Girls</small></div></div>
      <div class="cover-title">
        <h1>SUPPORT AND COUNSELING</h1>
        <h2>FOR WOMEN AND TEEN GIRLS</h2>
        <span class="pill">www.LanternSkye.com</span>
      </div>
    </article>
  </section>

  <section class="spread spread--inside">
    <article class="page page--services">
      <svg class="bg" viewBox="0 0 380 520">
        <defs>
          <linearGradient id="womanPhoto" x1="0" y1="0" x2="1" y2="1"><stop offset="0" stop-color="#9ab0b4"/><stop offset=".6" stop-color="#d8c2b1"/><stop offset="1" stop-color="#5d6d73"/></linearGradient>
          <linearGradient id="teenPhoto" x1="0" y1="0" x2="1" y2="1"><stop offset="0" stop-color="#e7eef2"/><stop offset=".6" stop-color="#b7c6d3"/><stop offset="1" stop-color="#6c8aa0"/></linearGradient>
        </defs>
        <path d="M0,478 C140,430 260,380 380,362" fill="none" stroke="var(--teal)" stroke-width="3"/>
        <circle cx="86" cy="428" r="80" fill="var(--teal)"/>
        <circle cx="86" cy="428" r="75" fill="url(#womanPhoto)" role="img" aria-label="Photo of a thoughtful young woman seated indoors"/>
        <circle cx="250" cy="348" r="58" fill="var(--teal)"/>
        <circle cx="250" cy="348" r="54" fill="url(#teenPhoto)" role="img" aria-label="Photo of a teenage girl resting on a chair"/>
      </svg>
      <div class="col" style="left:18px;top:34px;width:345px">
        <span class="tag">SERVICES :</span>
        <div class="body" style="margin-top:6px"><p>I believe that no two people are the same, and as such I tailor my therapy to meet the specific needs of my clients. Whether you are struggling with depression, anxiety, or another issue, I will help you find a way forward.</p></div>
      </div>
      <div class="col" style="left:18px;top:100px;width:170px">
        <p class="body">My practice specializes in working with women and teenage girls. Read more about my approach to the following issues:</p>
        <h3 class="heading">DEPRESSION :</h3>
        <ul class="bullets">
          <li>Do you have overwhelming feelings of sadness?</li>
          <li>Is it a struggle to get out of bed each day?</li>
          <li>Do you feel like nobody understands how you are feeling?</li>
          <li>Are you spending hours on social media comparing your life to others?</li>
        </ul>
        <p class="body">LanternSkye, LLC is all about meeting a person exactly where they are. Every journey is different, and there are tools that can help you manage these feelings and begin to heal. Contact us today to take the next step.</p>
      </div>
      <div class="col" style="left:200px;top:100px;width:165px">
        <h3 class="heading" style="margin-top:0">ANXIETY :</h3>
        <ul class="bullets">
          <li>Find your mind racing all day and all night?</li>
          <li>Can't get to sleep at night because you can't stop worrying?</li>
          <li>Do you wake up in the middle of the night and can't get back to sleep?</li>
          <li>Muscle tension, stomach problems, headaches?</li>
          <li>Panic attacks?</li>
        </ul>
        <p class="body">If you relate to these symptoms, LanternSkye, LLC can help you sort out the thoughts and worries that are disrupting your life. Contact us today to start feeling better.</p>
      </div>
    </article>

    <article class="page page--teen">
      <svg class="bg" viewBox="0 0 380 520">
        <defs><linearGradient id="mentorPhoto" x1="0" y1="0" x2="1" y2="1"><stop offset="0" stop-color="#dfe6ea"/><stop offset=".5" stop-color="#b9b3ab"/><stop offset="1" stop-color="#8fa4b3"/></linearGradient></defs>
        <path d="M0,400 C120,330 250,315 380,332" fill="none" stroke="var(--teal)" stroke-width="3"/>
        <path d="M0,408 C120,340 250,325 380,340 V520 H0 Z" fill="url(#mentorPhoto)" role="img" aria-label="Photo of a silver-haired woman looking out over the water"/>
      </svg>
      <div class="col" style="left:16px;top:60px;width:170px">
        <h3 class="heading">DEPRESSION :</h3>
        <ul class="bullets">
          <li>Are you a recent empty nester?</li>
          <li>Are you a new mother who is losing sight of who you used to be?</li>
          <li>Are you suddenly caring for an aging parent?</li>
          <li>Do you feel stuck in a season that is harder than expected?</li>
        </ul>
        <p class="body">It is normal to feel lost when life changes. Let us walk this path together. LanternSkye, LLC is here to help you grieve what was, embrace what is, and plan for what comes next with clarity and confidence.</p>
      </div>
      <div class="col" style="left:196px;top:22px;width:170px">
        <h3 class="heading">TEEN GIRL COUNSELING :</h3>
        <ul class="bullets">
          <li>Your daughter tells you everything is fine, but you know it's not.</li>
          <li>She's acting out, rebelling, or isolating in her room.</li>
          <li>You can tell she's struggling with friendships and self-image.</li>
          <li>You're desperate for her to be happy again but don't know how to help.</li>
        </ul>
        <p class="body">Teen girls today face pressures from school, friends, and social media that can feel overwhelming. They often hide their pain from the adults who love them most.</p>
        <p class="body">By helping teen girls build coping skills and self-worth, we give them the tools they need to thrive. Take the first step in getting your daughter the support she deserves today.</p>
      </div>
      <div class="col" style="left:16px;top:252px;width:170px">
        <p class="body">Teen Girl Counseling can help your teen create a meaningful and happy life. We are available to answer any questions and discuss your daughter's unique situation.</p>
      </div>
    </article>
  </section>

</main>
</body>
</html>
```